Re-design existing website and add products for sale.

Our current website is very basic and cluttered. (brightwillowcare.com.au)We want a modern looking website that is easy to navigate. We also want to start selling essential oils and crystal products, so there needs to be a separate page for this. Also needs to be easily edited as we need to change the monthly oracle card with the description. Would like calming colours as we are all about natural healing. Alongside the services listed there should be a button to book now which asks for their name, email, phone number ect. and adds it to the cart.

• Logo is still being designed, please leave a space for the logo which will basically be a lotus flower within a mandala.

```html
<!DOCTYPE html>
<html lang="en">
<head>
<meta charset="utf-8">
<title>Bright Willow Care</title>
<link rel="stylesheet" href="https://fonts.googleapis.com/css2?family=Pinyon+Script&family=Roboto:ital,wght@0,400;0,500;0,700;1,400&display=swap">
<style>
:root{
  --peach:#f4b49a;
  --peach-soft:#f9c9b0;
  --mint:#d4f2ee;
  --pink:#f4cbef;
  --teal:#2e5563;
  --teal-deep:#2b4f5b;
  --ink:#222;
  --grey:#666;
  --dark-panel:rgba(22,22,22,.92);
  --footer:#1e1e1e;
  --script:'Pinyon Script',cursive;
  --sans:'Roboto',Arial,sans-serif;
}
*{box-sizing:border-box;margin:0;padding:0}
html,body{width:1200px;height:3922px;overflow:hidden}
body{position:relative;font-family:var(--sans);color:var(--ink);background:#fff}
.abs{position:absolute}
.script{font-family:var(--script);font-weight:400}

/* header */
.site-header{position:absolute;left:0;top:0;width:1200px;height:110px;background:#fff;border-top:5px solid var(--peach-soft)}
.brand{position:absolute;left:112px;top:30px;font-family:var(--script);font-size:44px;color:#222}
.main-nav{position:absolute;left:554px;top:48px;display:flex;gap:24px;font-size:15px;font-weight:500}
.main-nav a{color:#222;text-decoration:none}
.main-nav a.active{color:var(--peach)}
.header-icons{position:absolute;left:965px;top:40px;display:flex;gap:6px}
.circle-icon{width:36px;height:36px;border-radius:50%;background:#1e1e1e;display:flex;align-items:center;justify-content:center}
.circle-icon.cart{background:var(--peach)}

/* hero */
.hero{position:absolute;left:0;top:110px;width:1200px;height:504px;
  background:radial-gradient(ellipse at 70% 60%,#7fb7e6 0%,transparent 35%),linear-gradient(110deg,#2a2a6e 0%,#5b3fa3 35%,#3b69b8 65%,#243a78 100%)}
.hero-title{position:absolute;left:353px;top:118px;width:520px;font-size:92px;line-height:88px;color:#fff}
.slider-arrow{position:absolute;width:44px;height:44px;border-radius:50%;background:#111;display:flex;align-items:center;justify-content:center}

/* section titles */
.section-title{position:absolute;left:0;width:1200px;text-align:center;font-family:var(--script);font-size:70px;color:#222}

/* products */
.product-grid{position:absolute;left:112px;top:824px;width:976px;height:353px;display:grid;grid-template-columns:repeat(4,244px);grid-template-rows:repeat(2,176.5px)}
.product-card{text-align:center;padding-top:30px}
.product-card h3{font-size:20px;font-weight:700;margin-bottom:12px}
.product-card p{font-size:14px;line-height:20px;color:#555;width:190px;margin:0 auto 14px}
.product-card .buy{font-size:15px;font-weight:700;text-decoration:underline;color:#222}
.product-card.mint{background:var(--mint)}
.product-card.pink{background:var(--pink)}
.product-card.peach{background:var(--peach-soft)}
.product-card.teal{background:var(--teal)}
.product-card.teal h3,.product-card.teal .buy{color:#fff}
.product-card.teal p{color:#d7e2e5}

/* services */
.services{position:absolute;left:0;top:1300px;width:1200px;height:773px;
  background:linear-gradient(100deg,#b79c8a 0%,#d9bfae 30%,#caa590 60%,#8a6a58 100%)}
.services-panel{position:absolute;left:340px;top:88px;width:520px;height:596px;background:var(--dark-panel);color:#fff}
.services-panel h2{text-align:center;font-family:var(--script);font-weight:400;font-size:60px;margin-top:24px}
.rule{width:70px;height:3px;background:var(--peach);margin:2px auto 0}
.service-list{position:absolute;left:73px;top:142px;width:380px;list-style:none}
.service-list li{display:flex;justify-content:space-between;height:34.6px;font-size:15px;font-weight:700}
.btn-peach{position:absolute;background:var(--peach);color:#222;font-size:15px;font-weight:700;display:flex;align-items:center;justify-content:center;gap:6px}

/* about */
.about{position:absolute;left:0;top:2073px;width:1200px;height:693px;background:var(--teal)}
.about-card{position:absolute;left:112px;top:118px;width:976px;height:457px;background:#fff}
.about-photo{position:absolute;left:11px;top:10px;width:434px;height:440px;
  background:radial-gradient(ellipse at 50% 30%,#f6b8e8 0%,#7a55c9 30%,#2c2e7a 65%,#0e1430 100%)}
.about-card h2{position:absolute;left:494px;top:34px;font-family:var(--script);font-weight:400;font-size:68px}
.about-text{position:absolute;left:494px;top:126px;width:436px;font-size:14px;line-height:26px;color:#666}
.about-text p+p{margin-top:14px}

/* testimonials */
.test-card{position:absolute;top:2998px;width:460px;height:207px;background:#fff;border-radius:12px;box-shadow:0 2px 12px rgba(0,0,0,.15)}
.test-card blockquote{position:absolute;left:40px;top:28px;width:390px;font-size:13px;line-height:26px;color:#666;font-style:italic}
.avatar{position:absolute;left:37px;top:119px;width:56px;height:56px;border-radius:50%;background:linear-gradient(#e3b07f,#b77a4a)}
.client-name{position:absolute;left:104px;top:128px;font-size:15px;font-weight:700}
.client-role{position:absolute;left:104px;top:154px;font-size:13px;font-style:italic;color:#666}
.nav-round{position:absolute;width:46px;height:46px;border-radius:50%;display:flex;align-items:center;justify-content:center}

/* contact */
.contact{position:absolute;left:0;top:3325px;width:1200px;height:400px;background:linear-gradient(90deg,#e8b3a0,#f0c8b8 50%,#e7b29f)}
.contact h2{position:absolute;left:112px;top:80px;font-family:var(--script);font-weight:400;font-size:56px;color:#222}
.contact-line{position:absolute;left:112px;display:flex;align-items:center;gap:18px;font-size:14px;line-height:22px;color:#333}
.contact-line .pin{width:38px;height:38px;border-radius:50%;background:#a9918a;display:flex;align-items:center;justify-content:center;flex:none}
.field{position:absolute;background:#fff;font-size:14px;color:#888;padding:10px 12px}
.robot{position:absolute;left:755px;top:3547px;display:flex;align-items:center;gap:14px;font-size:14px;color:#333}
.robot span.box{width:28px;height:28px;border:2px solid #555;background:#fff}
.badge{position:absolute;left:985px;top:3544px;width:40px;height:34px;border-radius:4px;background:#9bb0cc}
.submit{position:absolute;left:575px;top:3592px;width:330px;height:42px;background:var(--teal-deep);color:#fff;font-size:18px;font-weight:700;display:flex;align-items:center;justify-content:center}

/* footer */
.site-footer{position:absolute;left:0;top:3725px;width:1200px;height:197px;background:var(--footer);color:#fff}
.footer-icons{position:absolute;left:530px;top:57px;display:flex;gap:3px}
.footer-icons span{width:44px;height:44px;border-radius:50%;border:2px solid #fff}
.copyright{position:absolute;left:0;top:123px;width:1200px;text-align:center;font-size:15px;font-weight:500}
</style>
</head>
<body>

<header class="site-header">
  <div class="brand">Bright Willow Care</div>
  <nav class="main-nav">
    <a class="active" href="#">HOME</a><a href="#">ABOUT</a><a href="#">SERVICES</a><a href="#">PRODUCT</a><a href="#">CONTACT</a>
  </nav>
  <div class="header-icons">
    <span class="circle-icon cart"><svg width="16" height="16" viewBox="0 0 16 16"><path d="M3 6h10l-1 8H4z" fill="#222"/><path d="M5.5 6V4.5a2.5 2.5 0 0 1 5 0V6" stroke="#222" stroke-width="1.5" fill="none"/></svg></span>
    <span class="circle-icon"></span>
    <span class="circle-icon"></span>
  </div>
</header>

<section class="hero" role="img" aria-label="Hand holding an amethyst crystal against a glowing purple and blue energy background">
  <h1 class="hero-title script">Bright Willow Care</h1>
  <span class="slider-arrow" style="left:36px;top:229px"><svg width="14" height="14" viewBox="0 0 14 14"><path d="M9 2 4 7l5 5" stroke="#fff" stroke-width="2.5" fill="none"/></svg></span>
  <span class="slider-arrow" style="left:1118px;top:229px"><svg width="14" height="14" viewBox="0 0 14 14"><path d="M5 2l5 5-5 5" stroke="#fff" stroke-width="2.5" fill="none"/></svg></span>
</section>

<h2 class="section-title" style="top:690px">Our Products</h2>
<div class="product-grid">
  <div role="img" aria-label="Essential oil bottle with lavender" style="background:linear-gradient(160deg,#f1ece4,#c9a2cf 60%,#8e6aa8)"></div>
  <div class="product-card mint"><h3>CRYSTAL PRODUCT</h3><p>Lorem ipsum dolor consectetur adipiscing eiusmod temp.</p><span class="buy">Buy Now ➜</span></div>
  <div role="img" aria-label="Essential oil bottle with fresh mint leaves" style="background:linear-gradient(160deg,#e9eee6,#7fae6a 55%,#4d7a3e)"></div>
  <div class="product-card pink"><h3>CRYSTAL PRODUCT</h3><p>Lorem ipsum dolor consectetur adipiscing eiusmod temp.</p><span class="buy">Buy Now ➜</span></div>
  <div class="product-card peach"><h3>ESSENTIAL OIL1</h3><p>Lorem ipsum dolor consectetur adipiscing eiusmod temp.</p><span class="buy">Buy Now ➜</span></div>
  <div role="img" aria-label="Clear quartz crystal points" style="background:linear-gradient(160deg,#5d6168,#c5cbd0 50%,#3c4045)"></div>
  <div class="product-card teal"><h3>ESSENTIAL OIL1</h3><p>Lorem ipsum dolor consectetur adipiscing eiusmod temp.</p><span class="buy">Buy Now ➜</span></div>
  <div role="img" aria-label="Cluster of amethyst crystals" style="background:linear-gradient(160deg,#d8d2de,#8a6aa8 50%,#4c3466)"></div>
</div>

<section class="services" role="img" aria-label="Woman receiving a crystal healing treatment">
  <div class="services-panel">
    <h2>Our Services</h2>
    <div class="rule"></div>
    <ul class="service-list">
      <li><span>Reiki &amp; Seichim Healings</span><span>$51</span></li>
      <li><span>Energy Healing</span><span>$32</span></li>
      <li><span>Chakra Balancing</span><span>$28</span></li>
      <li><span>Energy Balancing</span><span>$67</span></li>
      <li><span>Past Life Clearing</span><span>$84</span></li>
      <li><span>Oracle Card Readings/Online Readings</span><span>$38</span></li>
      <li><span>Distant Healing</span><span>$64</span></li>
      <li><span>Reiki &amp; Seichim Workshops</span><span>$48</span></li>
      <li><span>Crystals &amp; Hand Made Jewellery Available</span><span>$32</span></li>
      <li><span>Essential Oil Roll On Blends Available</span><span>$81</span></li>
    </ul>
    <div class="btn-peach" style="left:190px;top:510px;width:139px;height:39px">BOOK NOW ➜</div>
  </div>
</section>

<section class="about">
  <div class="about-card">
    <div class="about-photo" role="img" aria-label="Silhouette of a person meditating in yoga pose under a colourful night sky"></div>
    <h2>About Us</h2>
    <div class="about-text">
      <p>Working together with you, I can help you achieve this. Whether through spiritual healing sessions using Reiki and Seichim, through Oracle Card Readings or a combination of these. I am passionate about using my knowledge and skills to help others struggling through their life journey.</p>
      <p>Reiki and Seichim workshops are also available for those who wish to learn Reiki or Seichim for themselves.</p>
    </div>
    <div class="btn-peach" style="left:494px;top:363px;width:160px;height:42px">BOOK NOW ➜</div>
  </div>
</section>

<h2 class="section-title" style="top:2860px">What Our Clients Say</h2>
<span class="nav-round" style="left:35px;top:3079px;background:#fff;border:1px solid #ddd"><svg width="14" height="14" viewBox="0 0 14 14"><path d="M9 2 4 7l5 5" stroke="#f4b49a" stroke-width="2.5" fill="none"/></svg></span>
<span class="nav-round" style="left:1119px;top:3079px;background:var(--peach)"><svg width="14" height="14" viewBox="0 0 14 14"><path d="M5 2l5 5-5 5" stroke="#222" stroke-width="2.5" fill="none"/></svg></span>
<article class="test-card" style="left:118px">
  <blockquote>“ Nemo enim ipsam voluptatem quia voluptas sit aspernatur aut odit aut fugit, sed quia consequuntur magni dolores eos qui ratione voluptatem sequi nesciunt. Neque porro quisquam ”</blockquote>
  <div class="avatar" role="img" aria-label="Client portrait"></div>
  <div class="client-name">Mara Ellison,</div>
  <div class="client-role">Owner - XYZ Company</div>
</article>
<article class="test-card" style="left:622px">
  <blockquote>“ Nemo enim ipsam voluptatem quia voluptas sit aspernatur aut odit aut fugit, sed quia consequuntur magni dolores eos qui ratione voluptatem sequi nesciunt. Neque porro quisquam ”</blockquote>
  <div class="avatar" role="img" aria-label="Client portrait"></div>
  <div class="client-name">Tobin Reyes,</div>
  <div class="client-role">Manager - ABC Company</div>
</article>

<section class="contact">
  <h2>Contact Us</h2>
  <div class="contact-line" style="top:156px"><span class="pin"><svg width="16" height="18" viewBox="0 0 16 18"><path d="M8 1a6 6 0 0 0-6 6c0 4.5 6 10 6 10s6-5.5 6-10a6 6 0 0 0-6-6z" fill="#fff"/><circle cx="8" cy="7" r="2.2" fill="#a9918a"/></svg></span><span>12 Wattle Lane,<br>Glenelg, SA 5045</span></div>
  <div class="contact-line" style="top:214px"><span class="pin"><svg width="16" height="16" viewBox="0 0 16 16"><path d="M3 1l3 3-2 2c1 2 3 4 5 5l2-2 3 3-2 3C7 14 2 9 1 3z" fill="#fff"/></svg></span><span>0400 000 123</span></div>
  <div class="contact-line" style="top:269px"><span class="pin"><svg width="16" height="12" viewBox="0 0 16 12"><rect x="1" y="1" width="14" height="10" fill="#fff"/><path d="M1 1l7 6 7-6" stroke="#a9918a" stroke-width="1.3" fill="none"/></svg></span><span>hello@brightwillowcare.com.au</span></div>
</section>
<div class="field" style="left:395px;top:3424px;width:329px;height:40px">Name</div>
<div class="field" style="left:395px;top:3477px;width:329px;height:40px">Email</div>
<div class="field" style="left:395px;top:3532px;width:329px;height:40px">Phone</div>
<div class="field" style="left:755px;top:3424px;width:330px;height:97px">Message</div>
<div class="robot"><span class="box"></span>I'm not a robot</div>
<div class="badge" aria-label="Verification badge"></div>
<div class="submit">SUBMIT NOW</div>

<footer class="site-footer">
  <div class="footer-icons"><span></span><span></span><span></span></div>
  <p class="copyright">Copyrights © 2019 Bright Willow Care. All Rights Reserved.</p>
</footer>

</body>
</html>
```